Brook Lanternfield Needs a new website!

We need a four page website for a new company based in San Francisco. We help companies connect better with their clients, employees, and vendors by implementing collaborative technology.
Similar Websites
Ridge Tinkers - http://www.ridgetinkers-example.com/
Mossvantage - http://www.mossvantage-example.com/ - I don't like the the rotating window or the pictures of people. I like the icons used to go to the next pages.
Color Combos
Blues and Yellows - http://www.example-palettes.com/schemes/96/Palette96.html
We prefer graphics over the actual pictures of people in the header. Pictures of people working together in the text is fine.
Web Page Layout
Index
Cloud Advisory Services
Email Everywhere
CRM Implementation
For detailed copy please see this link https://docs.example.com/a/quillmarten.com/document/d/7XkPqTrWmZsLnBvYhJdFgCaEuNoRiStUvWxYzAbCdEf/edit
Industry/Entity Type
It Company

```html
<!DOCTYPE html>
<html lang="en">
<head>
<meta charset="utf-8">
<title>Brook Lanternfield</title>
<link rel="stylesheet" href="https://fonts.googleapis.com/css2?family=Questrial&family=Open+Sans:wght@400;600&display=swap">
<style>
:root{
  --blue:#2160b3;
  --blue-deep:#1a4fa0;
  --navy:#0e3f98;
  --navy-dark:#0a2f78;
  --yellow:#f3c300;
  --page:#f3f4f4;
  --white:#ffffff;
  --text:#6d7075;
  --dark:#3a3d42;
  --rule:#dfe1e3;
}
*{box-sizing:border-box;margin:0;padding:0}
html,body{width:1200px;height:3435px;overflow:hidden}
body{background:var(--page);font-family:"Open Sans",Arial,sans-serif;color:var(--text);position:relative}
.abs{position:absolute}
h2{font-family:"Questrial",Arial,sans-serif;font-weight:400;font-size:26px;text-align:center;letter-spacing:1px}
.accent{color:var(--yellow)}
.blue{color:var(--blue)}
/* header */
.site-header{top:0;left:0;width:1200px;height:165px;background:var(--page);border-top:5px solid #e2e3e3}
.brand{left:126px;top:60px;display:flex;align-items:center;gap:12px}
.brand-dot{width:40px;height:40px;border-radius:50%;background:var(--blue)}
.brand-name{font-family:"Questrial",sans-serif;font-size:34px;color:var(--blue);font-weight:400}
.socials{display:flex;gap:6px}
.social{width:20px;height:20px;border-radius:50%;background:var(--blue)}
.header-socials{left:983px;top:36px}
.contact-line{font-size:13px;color:var(--blue);right:138px;display:flex;align-items:center;gap:8px;white-space:nowrap}
.search{left:935px;top:121px;width:188px;height:26px;border:1px solid #cfd2d5;border-radius:13px;background:#fff;font-size:11px;color:#999;padding:5px 12px}
.main-nav{top:165px;left:0;width:1200px;height:37px;background:var(--blue);border-bottom:4px solid var(--yellow);display:flex;padding-left:126px}
.main-nav a{color:#fff;text-decoration:none;font-size:13.5px;font-family:"Questrial",sans-serif;padding:10px 18px 0;height:33px;white-space:nowrap}
.main-nav a.active{background:#1a55a6}
/* hero */
.hero{top:202px;left:0;width:1200px;height:421px;background:linear-gradient(100deg,#1c2d4a 0%,#3f6aa3 35%,#8fb4d8 60%,#5d86b8 100%)}
.hero-panel{left:556px;top:75px;width:470px;height:256px;background:rgba(28,38,52,.85);padding:22px 37px;color:#fff}
.hero-panel h1{font-family:"Questrial",sans-serif;font-weight:400;font-size:56px;letter-spacing:2px;line-height:1;white-space:nowrap}
.hero-panel p{font-size:15px;line-height:25px;margin-top:12px}
.btn-more{display:inline-flex;align-items:center;gap:12px;background:var(--blue);color:#fff;font-size:13px;padding:6px 10px 6px 14px;margin-top:20px;white-space:nowrap}
.btn-more i{width:20px;height:20px;border-radius:50%;background:#fff;display:inline-block;position:relative}
.btn-more i::after{content:"";position:absolute;left:8px;top:6px;border-left:6px solid var(--blue);border-top:4px solid transparent;border-bottom:4px solid transparent}
.hero-dots{left:564px;top:400px;display:flex;gap:6px}
.hero-dots span{width:10px;height:10px;border-radius:50%;background:#8ea6c7}
.hero-dots span:first-child{background:#2b5aa0}
/* welcome */
.rule{height:1px;background:var(--rule)}
.intro{font-size:15.5px;line-height:25px;text-align:center}
.benefit{width:218px;height:321px;background:linear-gradient(#fff 60%,#ececec);box-shadow:0 1px 3px rgba(0,0,0,.12);text-align:center;padding:108px 18px 0}
.benefit h3{font-family:"Questrial",sans-serif;font-weight:400;font-size:16px;color:var(--dark);line-height:22px}
.benefit p{font-size:12px;line-height:18px;margin-top:10px}
.benefit-ring{width:152px;height:152px;border-radius:50%;background:#e6e7e8;padding:8px}
.benefit-ring div{width:136px;height:136px;border-radius:50%;background:var(--blue);display:flex;align-items:center;justify-content:center}
.btn-yellow{display:inline-block;background:var(--yellow);color:var(--dark);font-size:12px;padding:7px 0;text-align:center;white-space:nowrap}
.benefit .btn-yellow{position:absolute;left:54px;bottom:40px;width:110px}
/* segments */
.segments{top:1289px;left:0;width:1200px;height:406px;background:#f6f7f7}
.segment-list{left:178px;top:120px;width:470px;list-style:none}
.segment-list li{position:relative;padding-left:36px;font-size:14px;line-height:20px;margin-bottom:20px}
.segment-list li::before{content:"";position:absolute;left:0;top:2px;width:18px;height:18px;border-radius:50%;background:var(--blue)}
.segment-list li::after{content:"";position:absolute;left:5px;top:10px;width:8px;height:2px;background:#fff}
.monitor-screen{left:693px;top:113px;width:311px;height:205px;background:#2a2b2e;border-radius:6px;padding:14px}
.monitor-screen div{width:100%;height:100%;background:linear-gradient(135deg,#143563,#4b7db8 55%,#c9dbef)}
.monitor-stand{left:818px;top:318px;width:64px;height:22px;background:linear-gradient(#cfd1d3,#a7a9ab)}
.monitor-base{left:781px;top:338px;width:138px;height:8px;border-radius:4px;background:#b9bbbe}
/* what we do */
.services{top:1695px;left:0;width:1200px;height:542px;background:var(--blue)}
.services-notch{left:586px;top:-1px;border-left:16px solid transparent;border-right:16px solid transparent;border-top:20px solid #f6f7f7}
.services h2{color:#fff}
.services-intro{top:112px;left:0;width:1200px;color:#fff;text-align:center;font-size:15.5px;line-height:24px}
.service{width:180px;text-align:center;color:#fff;font-family:"Questrial",sans-serif;font-size:15px;line-height:19px}
.service-ring{width:96px;height:96px;border:2px solid #fff;border-radius:50%;margin:0 auto 20px;display:flex;align-items:center;justify-content:center}
/* about */
.person{width:282px;height:435px;background:linear-gradient(#fff 70%,#ececec);box-shadow:0 1px 3px rgba(0,0,0,.12);text-align:center;padding:92px 26px 0}
.person h3{font-family:"Questrial",sans-serif;font-weight:400;color:var(--blue);font-size:15px;white-space:nowrap}
.person p{font-size:12px;line-height:20px;margin-top:12px}
.portrait{width:128px;height:128px;border-radius:50%;border:4px solid var(--blue);background:radial-gradient(circle at 50% 40%,#d7b8a0,#8a6b55 60%,#4d4a52)}
.portrait.two{background:radial-gradient(circle at 50% 40%,#e6d2b0,#c4a577 55%,#7c8ea8)}
.btn-blue{display:inline-block;background:var(--blue-deep);color:#fff;font-size:12px;padding:5px 0;border-radius:12px;text-align:center;white-space:nowrap}
.person .btn-blue{position:absolute;left:93px;bottom:64px;width:96px}
.person .socials{position:absolute;left:109px;bottom:26px}
/* footer */
.site-footer{top:3027px;left:0;width:1200px;height:380px;background:var(--navy);border-top:22px solid #0b3587;color:#fff}
.footer-col h4{font-family:"Questrial",sans-serif;font-weight:400;font-size:14px;letter-spacing:.5px;margin-bottom:40px}
.footer-col ul{list-style:none}
.footer-col li{font-size:12.5px;line-height:30px;white-space:nowrap}
.footer-col li::before{content:"› ";font-weight:600}
.contact-list li::before{content:""}
.field{width:192px;height:30px;background:#fff;color:#555;font-size:11px;padding:6px 8px;margin-bottom:10px}
.field.area{height:86px}
.btn-submit{display:inline-block;background:#0a2c74;color:#fff;font-size:11px;padding:7px 22px;margin-top:8px}
.copyright{top:3407px;left:0;width:1200px;height:28px;background:var(--navy-dark);color:#fff;font-size:12px;padding:7px 0 0 153px}
</style>
</head>
<body>

<header class="site-header abs">
  <div class="brand abs"><span class="brand-dot"></span><span class="brand-name">Brook Lanternfield</span></div>
  <div class="socials header-socials abs"><span class="social"></span><span class="social"></span><span class="social"></span></div>
  <div class="contact-line abs" style="top:68px">
    <svg width="12" height="12" viewBox="0 0 12 12"><rect width="12" height="12" rx="2" fill="#2160b3"/><path d="M3 2.5h2l1 2-1.2 1a5 5 0 0 0 2.7 2.7l1-1.2 2 1v2a1 1 0 0 1-1 1A8 8 0 0 1 2 3.5a1 1 0 0 1 1-1z" fill="#fff" transform="scale(.8) translate(1.5 1.5)"/></svg>
    04-5550-2187</div>
  <div class="contact-line abs" style="top:89px;font-size:12px">
    <svg width="12" height="9" viewBox="0 0 12 9"><rect width="12" height="9" fill="#2160b3"/><path d="M0 0l6 5 6-5" stroke="#fff" fill="none"/></svg>
    youroffice@example.com</div>
  <div class="search abs">Keyword Search...</div>
</header>

<nav class="main-nav abs">
  <a class="active">Home</a><a>About us</a><a>Cloud Services</a><a>Cloud Advisory</a><a>Cloud Technology</a><a>Case Studies</a><a>Contact us</a>
</nav>

<section class="hero abs" role="img" aria-label="Header image: a businessman's hand touching a glowing cloud in a network of connected points">
  <div class="hero-panel abs">
    <h1>CRM Solutions</h1>
    <p>CRMs (Customer Relationship Management) can be complex and slow for employees to adopt. Accelerate your CRM adoption by selecting the right simple solution for your business.</p>
    <span class="btn-more">Read more <i></i></span>
  </div>
  <div class="hero-dots abs"><span></span><span></span><span></span><span></span></div>
</section>

<section class="welcome">
  <h2 class="abs" style="top:662px;left:0;width:1200px"><span class="accent">Welcome to</span> <span class="blue">Brook Lanternfield</span></h2>
  <div class="rule abs" style="top:707px;left:150px;width:900px"></div>
  <p class="intro abs" style="top:726px;left:165px;width:870px">Success in the cloud begins with a sound strategy. Start with a strong evaluation process. Then determine the right solution, proper implementation strategy and change management method. With the right transition you could recognize the benefits of the cloud:</p>

  <div class="benefit abs" style="left:179px;top:893px">
    <h3>Less infrastructure<br>and IT costs.</h3>
    <p>A cloud solution definitely means buying less hardware at your location. This also means less IT support.</p>
    <span class="btn-yellow">Read more</span>
  </div>
  <div class="benefit-ring abs" style="left:211px;top:842px"><div>
    <svg width="80" height="80" viewBox="0 0 80 80" fill="none" stroke="#fff" stroke-width="6"><path d="M14 40a26 26 0 0 1 46-16"/><path d="M66 40a26 26 0 0 1-46 16"/><path d="M52 20l10 4-2 11" stroke-linejoin="round"/><path d="M28 60l-10-4 2-11" stroke-linejoin="round"/><text x="40" y="50" font-size="28" text-anchor="middle" fill="#fff" stroke="none" font-family="Arial">$</text></svg>
  </div></div>

  <div class="benefit abs" style="left:499px;top:893px">
    <h3>Scalability</h3>
    <p>Cloud computing allows your business to easily upscale or downscale your IT requirements without expensive changes to your existing IT</p>
    <span class="btn-yellow">Read more</span>
  </div>
  <div class="benefit-ring abs" style="left:531px;top:842px"><div>
    <svg width="76" height="76" viewBox="0 0 76 76" fill="#fff"><path d="M6 6h22l-8 8 10 10-6 6-10-10-8 8z"/><path d="M70 6v22l-8-8-10 10-6-6 10-10-8-8z"/><path d="M6 70V48l8 8 10-10 6 6-10 10 8 8z"/><path d="M70 70H48l8-8-10-10 6-6 10 10 8-8z"/></svg>
  </div></div>

  <div class="benefit abs" style="left:820px;top:893px">
    <h3>Increase workforce<br>collaboration</h3>
    <p>Make it easier for your remote employees to be part of the organization. Give more flexibility to your staff</p>
    <span class="btn-yellow">Read more</span>
  </div>
  <div class="benefit-ring abs" style="left:852px;top:842px"><div>
    <svg width="80" height="80" viewBox="0 0 80 80" fill="#fff" stroke="#fff" stroke-width="4"><circle cx="40" cy="40" r="11"/><line x1="40" y1="29" x2="40" y2="10"/><line x1="40" y1="51" x2="40" y2="70"/><line x1="29" y1="40" x2="10" y2="40"/><line x1="51" y1="40" x2="70" y2="40"/><line x1="32" y1="32" x2="18" y2="18"/><line x1="48" y1="32" x2="62" y2="18"/><line x1="32" y1="48" x2="18" y2="62"/><line x1="48" y1="48" x2="62" y2="62"/><circle cx="40" cy="9" r="5"/><circle cx="40" cy="71" r="5"/><circle cx="9" cy="40" r="5"/><circle cx="71" cy="40" r="5"/><circle cx="17" cy="17" r="4"/><circle cx="63" cy="17" r="4"/><circle cx="17" cy="63" r="4"/><circle cx="63" cy="63" r="4"/></svg>
  </div></div>
</section>

<section class="segments abs">
  <h2 class="abs" style="top:28px;left:0;width:1200px"><span class="blue">Segments</span> <span class="accent">we serve</span></h2>
  <div class="rule abs" style="top:73px;left:150px;width:900px"></div>
  <ul class="segment-list abs">
    <li>Securities Services - Application development for hedge funds and asset management services.</li>
    <li>Service Organizations - SaaS recommendations to optimize workflow and stay focused on providing services.</li>
    <li>Retail - We are able to evaluate and recommend backoffice products to ensure efficiency for the front end.</li>
  </ul>
  <div class="monitor-screen abs"><div role="img" aria-label="Illustration of a business team working with glowing digital data"></div></div>
  <div class="monitor-stand abs"></div>
  <div class="monitor-base abs"></div>
</section>

<section class="services abs">
  <div class="services-notch abs"></div>
  <h2 class="abs" style="top:42px;left:0;width:1200px"><span class="accent">What</span> we do</h2>
  <p class="services-intro abs">We challenge the status quo by providing unique insights, emerging strategies and proven best practices.<br>Our unfaltering focus is on customer satisfaction. Our services include:</p>

  <div class="service abs" style="left:155px;top:240px">
    <div class="service-ring"><svg width="54" height="54" viewBox="0 0 54 54" fill="#fff"><path d="M27 12a12 12 0 0 0-7 22v5h14v-5a12 12 0 0 0-7-22z"/><rect x="21" y="41" width="12" height="3"/><rect x="22" y="46" width="10" height="3"/><g stroke="#f3c300" stroke-width="3"><line x1="27" y1="2" x2="27" y2="7"/><line x1="10" y1="9" x2="13" y2="12"/><line x1="44" y1="9" x2="41" y2="12"/><line x1="3" y1="24" x2="8" y2="24"/><line x1="46" y1="24" x2="51" y2="24"/></g></svg></div>Strategy</div>

  <div class="service abs" style="left:334px;top:240px">
    <div class="service-ring"><svg width="58" height="46" viewBox="0 0 58 46" fill="none" stroke="#fff" stroke-width="3"><path d="M14 40a11 11 0 0 1 0-22 15 15 0 0 1 29-2 12 12 0 0 1 1 24z"/><path d="M22 29a7 7 0 1 0 3-7" stroke="#f3c300"/><path d="M24 18l1 5-5 1" stroke="#f3c300"/></svg></div>Migration</div>

  <div class="service abs" style="left:510px;top:240px">
    <div class="service-ring"><svg width="56" height="56" viewBox="0 0 56 56"><circle cx="21" cy="33" r="11" fill="none" stroke="#fff" stroke-width="7" stroke-dasharray="4 3"/><circle cx="21" cy="33" r="6" fill="#fff"/><circle cx="39" cy="17" r="8" fill="none" stroke="#f3c300" stroke-width="6" stroke-dasharray="3 3"/><circle cx="39" cy="17" r="4" fill="#f3c300"/></svg></div>Implementation</div>

  <div class="service abs" style="left:691px;top:240px">
    <div class="service-ring"><svg width="56" height="56" viewBox="0 0 56 56"><path d="M12 22h24v-8l12 12-12 12v-8H12z" fill="#f3c300" transform="translate(0 -6)"/><path d="M44 36H20v-8L8 40l12 12v-8h24z" fill="#fff" transform="translate(0 -6)"/></svg></div>Integration</div>

  <div class="service abs" style="left:865px;top:240px">
    <div class="service-ring"><svg width="56" height="56" viewBox="0 0 56 56" fill="none" stroke-width="5"><path d="M10 26a18 18 0 0 1 32-10" stroke="#f3c300"/><path d="M44 8v10H34" stroke="#f3c300"/><path d="M46 30a18 18 0 0 1-32 10" stroke="#fff"/><path d="M12 48V38h10" stroke="#fff"/><path d="M20 22l6 6-6 6M29 22l6 6-6 6" stroke="#fff" stroke-width="3"/></svg></div>Adoption and<br>change management</div>

  <span class="btn-yellow abs" style="left:541px;top:457px;width:118px;height:38px;padding-top:11px;font-size:13px">Contact us</span>
</section>

<section class="about">
  <h2 class="abs" style="top:2272px;left:0;width:1200px"><span class="accent">About</span> <span class="blue">us</span></h2>
  <div class="rule abs" style="top:2317px;left:150px;width:900px"></div>
  <p class="intro abs" style="top:2338px;left:165px;width:870px">Tobin Ashcroft and Marisol Quade have combined their expertise and international team to offer quality advice on cloud strategies. Our objective is to provide guidance, thought leadership and strategic support to make the right decisions as you move your company forward.</p>

  <div class="person abs" style="left:268px;top:2519px">
    <h3>Tobin Ashcroft - Position</h3>
    <p>IT services consultant and infrastructure architect with a strong background in a wide range of IT infrastructure and application development exposure. Most effective designing and managing infrastructure and IT services in start-ups, high tech companies, and companies undergoing growth and structural change.</p>
    <span class="btn-blue">Read more</span>
    <div class="socials"><span class="social"></span><span class="social"></span><span class="social"></span></div>
  </div>
  <div class="portrait abs" style="left:345px;top:2459px" role="img" aria-label="Portrait photo of Tobin Ashcroft"></div>

  <div class="person abs" style="left:648px;top:2519px">
    <h3>Marisol Quade - Position</h3>
    <p>Deep experienced in delivering a wide variety of IT business applications on time and within budget from very large to very small companies. Seeing hyper-growth operations as well as streamlining steady business practices in the financial services, communications, media, retail industries, I have managed implementations and daily opera-</p>
    <span class="btn-blue">Read more</span>
    <div class="socials"><span class="social"></span><span class="social"></span><span class="social"></span></div>
  </div>
  <div class="portrait two abs" style="left:725px;top:2459px" role="img" aria-label="Portrait photo of Marisol Quade"></div>
</section>

<footer class="site-footer abs">
  <div class="footer-col abs" style="left:160px;top:68px">
    <h4>Navigation</h4>
    <ul><li>Cloud Services</li><li>Cloud Advisory</li><li>Cloud Technology</li><li>Case Studies</li></ul>
  </div>
  <div class="footer-col abs" style="left:389px;top:68px">
    <h4>Useful Info</h4>
    <ul><li>FAQ</li><li>Sitemap</li><li>Terms &amp; Agreement</li><li>Privacy Policy</li></ul>
  </div>
  <div class="footer-col abs" style="left:607px;top:68px">
    <h4>Contact us</h4>
    <ul class="contact-list"><li>✉ Youroffice@example.com</li><li>☎ 04-5550-219</li></ul>
    <div class="socials" style="margin-top:6px"><span class="social" style="background:#fff"></span><span class="social" style="background:#fff"></span><span class="social" style="background:#fff"></span></div>
  </div>
  <div class="footer-col abs" style="left:852px;top:68px">
    <h4 style="margin-bottom:30px">Quick Message</h4>
    <div class="field">Firstname</div>
    <div class="field">Email address</div>
    <div class="field area">Message</div>
    <span class="btn-submit">SUBMIT</span>
  </div>
</footer>
<div class="copyright abs">Copyright © 2014 Brook Lanternfield</div>

</body>
</html>
```